Business card for Mortgage broker business

I have already had the logo designed and am needing a great looking business card. My business focus is on servicing clients who may not be able to obtain finance through traditional lenders due to bad credit, short term employment or they just don't fit the banks profile. It needs to be professional, trust worthy but also have a caring fell about it.
I have provided files showing the green and black logo, the white logo(on white background so the file looks blank) and also a file with the white logo with a background of leaves that was made up which will probably be used for a website header.

Industry/Entity Type

Finance

Contact Information for Business Card

Marcus Dolbey
Managing Director, Accredited Finance Broker(AFB)
Po Box 287, Pakenham VIC 3810
marcus@kestrelfinance.com.au
www.kestrelfinance.com.au
0438 162 507

Requirements
Nice to have
• I have added a picture of myself as I would like to see some designs with the pic in it, but I'm not sure if I want it on there with the logo's or just the logo's

```html
<!DOCTYPE html>
<html lang="en">
<head>
<meta charset="UTF-8">
<title>Kestrel Finance – Business Card</title>
<link rel="stylesheet" href="https://fonts.googleapis.com/css2?family=Fira+Sans:wght@300;400&display=swap">
<style>
  :root {
    --page-bg: #d8dbd8;
    --card-light: #f1f3f1;
    --card-light-edge: #e2e6e3;
    --brand-green: #1e5a3b;
    --green-deep: #0e3a24;
    --green-mid: #1f5d3d;
    --edge-dark: #1a1d1b;
    --text-on-green: #e9efe9;
    --text-soft: #cfdcd2;
    --card-border: #b9bfba;
  }
  * { margin: 0; padding: 0; box-sizing: border-box; }
  html, body {
    width: 1200px;
    height: 969px;
    overflow: hidden;
    background: var(--page-bg);
    font-family: "Fira Sans", Arial, sans-serif;
  }
  .canvas {
    position: relative;
    width: 1200px;
    height: 969px;
  }
  .business-card {
    position: absolute;
    left: 100px;
    top: 200px;
    width: 1000px;
    height: 568px;
    background: linear-gradient(135deg, var(--card-light) 0%, var(--card-light-edge) 100%);
    border: 1px solid var(--card-border);
    overflow: hidden;
    box-shadow: 0 10px 30px rgba(0,0,0,0.15);
  }
  .card-wave {
    position: absolute;
    inset: 0;
    width: 1000px;
    height: 568px;
  }
  .brand-name {
    position: absolute;
    left: 58px;
    top: 160px;
    font-size: 56px;
    font-weight: 400;
    color: var(--brand-green);
    letter-spacing: 0.5px;
  }
  .contact-block {
    position: absolute;
    right: 46px;
    top: 0;
    width: 560px;
    height: 568px;
    color: var(--text-on-green);
    text-align: right;
  }
  .holder-name {
    position: absolute;
    right: 0;
    top: 56px;
    font-size: 33px;
    font-weight: 400;
    letter-spacing: 1.5px;
    text-transform: uppercase;
  }
  .holder-title {
    position: absolute;
    right: 0;
    top: 106px;
    font-size: 20px;
    font-weight: 300;
    line-height: 28px;
    letter-spacing: 1.1px;
    text-transform: uppercase;
  }
  .postal-address {
    position: absolute;
    right: 0;
    top: 244px;
    font-size: 25px;
    font-weight: 300;
    line-height: 36px;
    font-style: normal;
  }
  .contact-list {
    position: absolute;
    right: 0;
    top: 334px;
    list-style: none;
  }
  .contact-item {
    display: flex;
    justify-content: flex-end;
    align-items: center;
    height: 40px;
    font-size: 24px;
    font-weight: 300;
    color: var(--text-soft);
  }
  .contact-icon {
    width: 26px;
    height: 26px;
    margin-left: 16px;
    flex: none;
  }
</style>
</head>
<body>
<main class="canvas">
  <section class="business-card" aria-label="Kestrel Finance business card">
    <svg class="card-wave" viewBox="0 0 1000 568" aria-hidden="true">
      <defs>
        <linearGradient id="greenPanel" x1="0" y1="0" x2="1" y2="1">
          <stop offset="0" stop-color="#1f5d3d"/>
          <stop offset="0.55" stop-color="#174d31"/>
          <stop offset="1" stop-color="#0e3a24"/>
        </linearGradient>
      </defs>
      <path d="M 718 0 L 1000 0 L 1000 568 L 300 568 C 450 540, 520 430, 570 262 C 610 120, 650 20, 718 0 Z" fill="#1a1d1b"/>
      <path d="M 738 0 L 1000 0 L 1000 568 L 335 568 C 475 540, 545 430, 592 262 C 632 120, 672 20, 738 0 Z" fill="url(#greenPanel)"/>
    </svg>

    <p class="brand-name">Kestrel Finance</p>

    <div class="contact-block">
      <h1 class="holder-name">Marcus Dolbey</h1>
      <p class="holder-title">Managing Director,<br>Accredited Finance<br>Broker (AFB)</p>
      <address class="postal-address">Po Box 287<br>Pakenham VIC 3810</address>
      <ul class="contact-list">
        <li class="contact-item">0438 162 507
          <svg class="contact-icon" viewBox="0 0 24 24" aria-label="Phone"><path fill="#e9efe9" d="M3 9c0-3 4-5 9-5s9 2 9 5v1h-4V8c-1-.8-3-1.2-5-1.2S8 7.2 7 8v2H3zM7 11h10l3 8H4z"/><circle cx="12" cy="15" r="2" fill="#174d31"/></svg>
        </li>
        <li class="contact-item">marcus@kestrelfinance.com.au
          <svg class="contact-icon" viewBox="0 0 24 24" aria-label="Email"><rect x="2" y="5" width="20" height="14" fill="#e9efe9"/><path d="M2 5l10 8 10-8" fill="none" stroke="#174d31" stroke-width="1.6"/></svg>
        </li>
        <li class="contact-item">www.kestrelfinance.com.au
          <svg class="contact-icon" viewBox="0 0 24 24" aria-label="Website"><circle cx="12" cy="12" r="10" fill="#e9efe9"/><path d="M12 2v20M2 12h20M12 2c-4 3-4 17 0 20M12 2c4 3 4 17 0 20" fill="none" stroke="#174d31" stroke-width="1.3"/></svg>
        </li>
      </ul>
    </div>
  </section>
</main>
</body>
</html>
```